Demo Screens Needed for Recruiting with AI App

We are in the process of raising money for our startup called PylonGrove. We need demos to show investors what we're trying to do with images. We really love the simplicity and modern look of the Lantern App and want something similar. We will have the "swipe" functionality similar to Kindle as well. The sample images I've attached are only for caregivers but long term this will be for all industries. There will also be a rewards page for loyalty membership. The current landing page is www.pylongrove.example. That will show you the color scheme and logo.

```html
<!DOCTYPE html>
<html lang="en">
<head>
<meta charset="utf-8">
<title>PylonGrove — Demo Screens</title>
<link rel="stylesheet" href="https://fonts.googleapis.com/css2?family=Plus+Jakarta+Sans:wght@300;400;500;600;700&family=Rajdhani:wght@500&display=swap">
<style>
:root{
  --bg-top:#15243a;
  --bg-bottom:#1c1533;
  --label:#3fb3e6;
  --ink:#151821;
  --muted:#6b7280;
  --line:#eceef3;
  --panel:#f4f5f8;
  --white:#ffffff;
  --brand-blue:#3fa6e8;
  --brand-purple:#7b4fe0;
  --pink:#e6336e;
  --star:#4f6ee6;
  --wave:#f6b51c;
  --online:#22c55e;
  --verified:#3b82f6;
  --splash-a:#1a1433;
  --splash-b:#1b3a4e;
  --photo-a:#6b4a3a;
  --photo-b:#c9553a;
  --photo-c:#3c2f3a;
  --park-a:#5f8a4a;
  --park-b:#2f4a2a;
  --park-c:#8a7d6e;
}
*{box-sizing:border-box;margin:0;padding:0}
html,body{width:981px;height:1200px;overflow:hidden}
body{
  font-family:"Plus Jakarta Sans",sans-serif;
  background:linear-gradient(160deg,var(--bg-top) 0%,#17203a 55%,var(--bg-bottom) 100%);
  color:var(--ink);
}
.board{display:flex;flex-direction:column;gap:50px;padding:36px 0 0}
.row{display:flex;justify-content:center;gap:60px}
.slot{display:flex;flex-direction:column;align-items:center;gap:12px}
.slot-label{
  font-family:"Rajdhani",sans-serif;font-weight:500;font-size:13px;
  letter-spacing:.42em;color:var(--label);text-transform:uppercase;
}
.screen{
  width:244px;height:520px;border-radius:30px;overflow:hidden;position:relative;
  background:var(--white);display:flex;flex-direction:column;
  box-shadow:0 10px 30px rgba(0,0,0,.35);
}
.status{height:30px;display:flex;align-items:center;justify-content:space-between;padding:4px 20px 0 26px;font-size:10px;font-weight:600;flex-shrink:0}
.status-icons{display:flex;gap:4px;align-items:center}
.home-bar{position:absolute;bottom:7px;left:50%;transform:translateX(-50%);width:84px;height:3px;border-radius:2px;background:var(--ink)}

/* splash */
.splash{background:linear-gradient(180deg,var(--splash-a) 0%,#1d2a48 45%,var(--splash-b) 100%);color:var(--white)}
.splash .home-bar{background:var(--white)}
.splash-art{position:absolute;left:30px;top:120px;width:190px;height:200px;border-radius:50%;
  background:radial-gradient(circle at 40% 45%,rgba(120,140,190,.28),rgba(40,50,90,0) 70%)}
.wordmark{margin-top:90px;text-align:center;font-weight:300;font-size:21px;letter-spacing:.1em;position:relative}
.tagline{margin-top:150px;text-align:center;font-size:12px;line-height:1.55;position:relative}
.tagline strong{font-weight:700;display:block}
.auth{margin:26px 20px 0;display:flex;flex-direction:column;gap:8px;position:relative}
.auth-btn{height:28px;border-radius:14px;background:var(--white);color:var(--ink);font-size:8.5px;font-weight:600;display:flex;align-items:center;justify-content:center;gap:6px}
.auth-btn .dot{width:8px;height:8px;border-radius:50%;background:var(--ink)}
.auth-btn.mobile{background:linear-gradient(90deg,var(--brand-blue),var(--brand-purple));color:var(--white)}
.legal{margin:24px 28px 0;text-align:center;font-size:7px;line-height:1.7;color:#d5dbe8;position:relative}
.legal a{color:var(--label);text-decoration:none}

/* explore */
.topbar{height:32px;display:flex;align-items:center;justify-content:space-between;padding:0 14px;flex-shrink:0}
.card{position:relative;display:flex;flex-direction:column;flex:1;min-height:0}
.card.inset{margin:0 9px;border-radius:12px;overflow:hidden;box-shadow:0 2px 10px rgba(0,0,0,.08)}
.photo{position:relative;background:linear-gradient(160deg,var(--photo-c) 0%,var(--photo-a) 45%,var(--photo-b) 100%)}
.photo.park{background:linear-gradient(170deg,var(--park-a) 0%,var(--park-b) 55%,var(--park-c) 100%)}
.card-head{position:absolute;top:6px;left:9px;right:9px;display:flex;justify-content:space-between;color:var(--white)}
.card-name{font-size:10.5px;font-weight:600;display:flex;align-items:center;gap:3px}
.card-active{font-size:6px;display:flex;align-items:center;gap:3px;margin-top:1px}
.online{width:4px;height:4px;border-radius:50%;background:var(--online)}
.more{font-size:12px;letter-spacing:1px;line-height:8px}
.actions{position:absolute;bottom:10px;left:0;right:0;display:flex;justify-content:center;gap:10px}
.act{width:38px;height:38px;border-radius:50%;background:var(--white);display:flex;align-items:center;justify-content:center;box-shadow:0 2px 6px rgba(0,0,0,.25)}
.act.wave{background:var(--wave)}
.prompt{padding:10px 12px 12px;background:var(--white)}
.prompt-q{font-size:7px;color:var(--muted)}
.prompt-a{margin-top:6px;font-size:10.5px;font-weight:700;line-height:1.45}
.tabs{height:40px;display:flex;align-items:center;justify-content:space-around;padding:0 10px 8px;flex-shrink:0}
.tab-brand{width:11px;height:11px;border-radius:3px;background:var(--brand-purple)}
.avatar{width:12px;height:12px;border-radius:50%;background:linear-gradient(135deg,#8a6a5a,#3a3038)}

/* profile */
.profile-head{height:36px;display:flex;align-items:center;justify-content:space-between;padding:0 14px;flex-shrink:0}
.profile-title{text-align:center}
.profile-name{font-size:12px;font-weight:600;display:flex;align-items:center;gap:3px;justify-content:center}
.profile-active{font-size:6px;color:var(--muted);display:flex;align-items:center;gap:3px;justify-content:center}
.facts{padding:6px 10px 8px;flex-shrink:0}
.facts.boxed{margin:4px 9px 0;border-radius:10px;background:var(--white);box-shadow:0 1px 6px rgba(0,0,0,.08)}
.fact{height:27px;display:flex;align-items:center;gap:6px;font-size:7px;font-weight:500}
.fact svg{flex-shrink:0}
.stats{justify-content:space-between}
.stat{display:flex;align-items:center;gap:5px}
.chip{padding:2px 6px;border-radius:7px;background:var(--panel);font-size:6.5px}
.profile-photo{flex:1;position:relative}
.profile-photo.inset{margin:6px 9px 0;border-radius:10px 10px 0 0;overflow:hidden}
</style>
</head>
<body>
<svg width="0" height="0" style="position:absolute">
  <defs>
    <symbol id="ic-signal" viewBox="0 0 14 10"><rect x="0" y="6" width="2.5" height="4" fill="currentColor"/><rect x="4" y="4" width="2.5" height="6" fill="currentColor"/><rect x="8" y="2" width="2.5" height="8" fill="currentColor"/><rect x="12" y="0" width="2" height="10" fill="currentColor"/></symbol>
    <symbol id="ic-wifi" viewBox="0 0 14 10"><path d="M1 3.5a9 9 0 0 1 12 0M3.2 5.8a6 6 0 0 1 7.6 0M5.4 8a3 3 0 0 1 3.2 0" fill="none" stroke="currentColor" stroke-width="1.5" stroke-linecap="round"/></symbol>
    <symbol id="ic-battery" viewBox="0 0 20 10"><rect x="0.5" y="0.5" width="17" height="9" rx="2.5" fill="none" stroke="currentColor" opacity=".5"/><rect x="2" y="2" width="14" height="6" rx="1.5" fill="currentColor"/><rect x="18.5" y="3.5" width="1.5" height="3" rx=".7" fill="currentColor" opacity=".5"/></symbol>
    <symbol id="ic-undo" viewBox="0 0 16 16"><path d="M3 8a5 5 0 1 0 1.5-3.6M3 2.5v2.5h2.5" fill="none" stroke="#9aa1ad" stroke-width="1.4" stroke-linecap="round"/></symbol>
    <symbol id="ic-filter" viewBox="0 0 16 16"><path d="M2 4h12M2 8h12M2 12h12" stroke="#9aa1ad" stroke-width="1.3"/><circle cx="10" cy="4" r="1.6" fill="#fff" stroke="#9aa1ad"/><circle cx="5" cy="8" r="1.6" fill="#fff" stroke="#9aa1ad"/><circle cx="11" cy="12" r="1.6" fill="#fff" stroke="#9aa1ad"/></symbol>
    <symbol id="ic-check" viewBox="0 0 10 10"><circle cx="5" cy="5" r="5" fill="var(--verified)"/><path d="M3 5.2l1.4 1.4L7.2 3.8" fill="none" stroke="#fff" stroke-width="1.2"/></symbol>
    <symbol id="ic-x" viewBox="0 0 16 16"><path d="M3 3l10 10M13 3L3 13" stroke="var(--pink)" stroke-width="2" stroke-linecap="round"/></symbol>
    <symbol id="ic-star" viewBox="0 0 16 16"><path d="M8 1.2l2 4.3 4.7.5-3.5 3.2 1 4.6L8 11.5 3.8 13.8l1-4.6L1.3 6l4.7-.5z" fill="var(--star)"/></symbol>
    <symbol id="ic-wave" viewBox="0 0 16 16"><path d="M5 14c-2-1.5-2.5-4-1.5-6L6 3.5c.4-.8 1.6-.4 1.4.5L7 6l3-4.5c.5-.7 1.5 0 1.1.8L9 6.5l3-3.5c.6-.6 1.5.1 1 .8L10.3 8l2.2-2c.6-.5 1.4.2.9.8L10 11c-1.5 2.5-3.5 3.8-5 3z" fill="#e08a00"/></symbol>
    <symbol id="ic-trophy" viewBox="0 0 16 16"><path d="M5 2h6v4a3 3 0 0 1-6 0zM8 9v3M5.5 14h5M5 3H2.5a2 2 0 0 0 2.5 3M11 3h2.5a2 2 0 0 1-2.5 3" fill="none" stroke="#a3a9b5" stroke-width="1.3"/></symbol>
    <symbol id="ic-search" viewBox="0 0 16 16"><circle cx="7" cy="7" r="4.5" fill="none" stroke="#a3a9b5" stroke-width="1.4"/><path d="M10.5 10.5L14 14" stroke="#a3a9b5" stroke-width="1.4" stroke-linecap="round"/></symbol>
    <symbol id="ic-chat" viewBox="0 0 16 16"><path d="M8 2.5a5.5 5.5 0 0 0-4.8 8.2L2.5 13.5l2.9-.8A5.5 5.5 0 1 0 8 2.5z" fill="none" stroke="#a3a9b5" stroke-width="1.4"/></symbol>
    <symbol id="ic-close" viewBox="0 0 16 16"><path d="M4 4l8 8M12 4l-8 8" stroke="#9aa1ad" stroke-width="1.3" stroke-linecap="round"/></symbol>
    <symbol id="ic-bag" viewBox="0 0 16 16"><rect x="2" y="5" width="12" height="9" rx="2" fill="#aeb4bf"/><path d="M6 5V3.5h4V5" fill="none" stroke="#aeb4bf" stroke-width="1.3"/></symbol>
    <symbol id="ic-person" viewBox="0 0 16 16"><path d="M3 13l1-6h8l1 6z" fill="none" stroke="#aeb4bf" stroke-width="1.3"/><circle cx="8" cy="4" r="2" fill="none" stroke="#aeb4bf" stroke-width="1.3"/></symbol>
    <symbol id="ic-coin" viewBox="0 0 16 16"><circle cx="8" cy="8" r="6.5" fill="#aeb4bf"/><text x="8" y="11" font-size="8" text-anchor="middle" fill="#fff" font-family="sans-serif">$</text></symbol>
    <symbol id="ic-rate" viewBox="0 0 16 16"><path d="M8 1.5l2 4.2 4.6.5-3.4 3.1 1 4.5L8 11.5 3.8 13.8l1-4.5L1.4 6.2 6 5.7z" fill="#aeb4bf"/></symbol>
    <symbol id="ic-pin" viewBox="0 0 16 16"><path d="M8 15s5-5 5-8.5a5 5 0 0 0-10 0C3 10 8 15 8 15z" fill="#aeb4bf"/><circle cx="8" cy="6.5" r="1.8" fill="#fff"/></symbol>
    <symbol id="ic-lang" viewBox="0 0 16 16"><path d="M2 4h7M5.5 2.5V4M3.5 4c.5 2.5 2 4 4 5M7.5 4c-.5 2.5-2 4-4 5M9 14l2.5-6 2.5 6M10 12h3" fill="none" stroke="#aeb4bf" stroke-width="1.1"/></symbol>
    <symbol id="ic-degree" viewBox="0 0 16 16"><rect x="2" y="2.5" width="12" height="10" rx="1.5" fill="#aeb4bf"/><path d="M5 6h6M5 8.5h4" stroke="#fff" stroke-width="1.1"/></symbol>
    <symbol id="ic-child" viewBox="0 0 16 16"><circle cx="8" cy="3" r="1.8" fill="#aeb4bf"/><path d="M3 6h10M8 6v4l-2.5 4M8 10l2.5 4" fill="none" stroke="#aeb4bf" stroke-width="1.4" stroke-linecap="round"/></symbol>
    <symbol id="ic-kit" viewBox="0 0 16 16"><rect x="1.5" y="4.5" width="13" height="9" rx="1.5" fill="#aeb4bf"/><path d="M6 4.5V3h4v1.5" fill="none" stroke="#aeb4bf" stroke-width="1.2"/></symbol>
    <symbol id="ic-clock" viewBox="0 0 16 16"><circle cx="8" cy="8" r="6" fill="none" stroke="#aeb4bf" stroke-width="1.3"/><path d="M8 4.5V8l2.5 1.5" fill="none" stroke="#aeb4bf" stroke-width="1.3"/></symbol>
    <symbol id="ic-warn" viewBox="0 0 16 16"><path d="M8 2l6.5 12h-13z" fill="#aeb4bf"/><path d="M8 6.5v3.5M8 11.5v.5" stroke="#fff" stroke-width="1.3"/></symbol>
  </defs>
</svg>

<main class="board">
  <div class="row">
    <!-- splash -->
    <section class="slot">
      <h2 class="slot-label">Splash Screen</h2>
      <div class="screen splash">
        <div class="status"><span>9:41</span><span class="status-icons"><svg width="12" height="8"><use href="#ic-signal"/></svg><svg width="12" height="8"><use href="#ic-wifi"/></svg><svg width="16" height="8"><use href="#ic-battery"/></svg></span></div>
        <div class="splash-art" role="img" aria-label="Faint abstract artwork behind the brand name"></div>
        <div class="wordmark">PYLONGROVE</div>
        <p class="tagline">Unlocking the power of<strong>Meaningful Connections</strong></p>
        <div class="auth">
          <div class="auth-btn"><span class="dot"></span>Continue with Orchard</div>
          <div class="auth-btn"><span class="dot"></span>Continue with Searchly</div>
          <div class="auth-btn mobile"><svg width="7" height="10" viewBox="0 0 7 10"><rect x=".6" y=".6" width="5.8" height="8.8" rx="1.2" fill="none" stroke="#fff" stroke-width="1.1"/></svg>Use mobile number</div>
        </div>
        <p class="legal">By signing up, you agree to our <a>Terms</a> and <a>Privacy Policy</a>. We protect your personal data.</p>
        <div class="home-bar"></div>
      </div>
    </section>

    <!-- explore v1 -->
    <section class="slot">
      <h2 class="slot-label">Explore V1</h2>
      <div class="screen">
        <div class="status"><span>9:41</span><span class="status-icons"><svg width="12" height="8"><use href="#ic-signal"/></svg><svg width="12" height="8"><use href="#ic-wifi"/></svg><svg width="16" height="8"><use href="#ic-battery"/></svg></span></div>
        <div class="topbar"><svg width="13" height="13"><use href="#ic-undo"/></svg><svg width="13" height="13"><use href="#ic-filter"/></svg></div>
        <article class="card inset">
          <div class="photo" style="height:296px" role="img" aria-label="Photo of a smiling caregiver with paint-covered hands in a colourful playroom">
            <div class="card-head"><div><div class="card-name">Marisol, $25/h <svg width="8" height="8"><use href="#ic-check"/></svg></div><div class="card-active"><span class="online"></span>Active today</div></div><span class="more">···</span></div>
            <div class="actions"><span class="act"><svg width="14" height="14"><use href="#ic-x"/></svg></span><span class="act"><svg width="16" height="16"><use href="#ic-star"/></svg></span><span class="act wave"><svg width="18" height="18"><use href="#ic-wave"/></svg></span></div>
          </div>
          <div class="prompt"><p class="prompt-q">One thing I prioritize in childcare is</p><p class="prompt-a">Creating a fun and engaging atmosphere where children can explore, play, and express themselves creatively</p></div>
        </article>
        <nav class="tabs"><span class="tab-brand"></span><svg width="12" height="12"><use href="#ic-trophy"/></svg><svg width="12" height="12"><use href="#ic-search"/></svg><svg width="12" height="12"><use href="#ic-chat"/></svg><span class="avatar"></span></nav>
        <div class="home-bar"></div>
      </div>
    </section>

    <!-- profile v1 -->
    <section class="slot">
      <h2 class="slot-label">Profile V1</h2>
      <div class="screen" style="background:var(--panel)">
        <div class="status" style="background:var(--white)"><span>9:41</span><span class="status-icons"><svg width="12" height="8"><use href="#ic-signal"/></svg><svg width="12" height="8"><use href="#ic-wifi"/></svg><svg width="16" height="8"><use href="#ic-battery"/></svg></span></div>
        <header class="profile-head" style="background:var(--white)"><svg width="12" height="12"><use href="#ic-close"/></svg><div class="profile-title"><div class="profile-name">Marisol <svg width="9" height="9"><use href="#ic-check"/></svg></div><div class="profile-active"><span class="online"></span>Active</div></div><span class="more" style="color:#9aa1ad">···</span></header>
        <ul class="facts boxed" style="list-style:none">
          <li class="fact stats"><span class="stat"><svg width="10" height="10"><use href="#ic-bag"/></svg>10 yrs</span><span class="stat"><svg width="10" height="10"><use href="#ic-person"/></svg>Female</span><span class="stat"><svg width="10" height="10"><use href="#ic-coin"/></svg>25–35/h</span><span class="stat"><svg width="10" height="10"><use href="#ic-rate"/></svg>4.8</span></li>
          <li class="fact"><svg width="10" height="10"><use href="#ic-pin"/></svg>Cedar Vale, California</li>
          <li class="fact"><svg width="10" height="10"><use href="#ic-lang"/></svg>English, Spanish, Mandarin</li>
          <li class="fact"><svg width="10" height="10"><use href="#ic-degree"/></svg>Bachelor's Degree</li>
          <li class="fact"><svg width="10" height="10"><use href="#ic-child"/></svg>Age groups: <span class="chip">0–11 mo</span><span class="chip">1–3 yrs</span><span class="chip">4–5 yrs</span></li>
          <li class="fact"><svg width="10" height="10"><use href="#ic-kit"/></svg>CPR Trained, Special Needs Care</li>
          <li class="fact"><svg width="10" height="10"><use href="#ic-clock"/></svg>Full time, open to part time</li>
          <li class="fact"><svg width="10" height="10"><use href="#ic-warn"/></svg>Comfortable with pets, meal prep</li>
        </ul>
        <div class="profile-photo inset photo park" role="img" aria-label="Photo of the caregiver in a cap sitting in a sunny park">
          <div class="actions"><span class="act"><svg width="14" height="14"><use href="#ic-x"/></svg></span><span class="act"><svg width="16" height="16"><use href="#ic-star"/></svg></span><span class="act wave"><svg width="18" height="18"><use href="#ic-wave"/></svg></span></div>
        </div>
        <div class="home-bar" style="background:var(--white)"></div>
      </div>
    </section>
  </div>

  <div class="row">
    <!-- explore v2 -->
    <section class="slot">
      <h2 class="slot-label">Explore V2</h2>
      <div class="screen">
        <div class="status"><span>9:41</span><span class="status-icons"><svg width="12" height="8"><use href="#ic-signal"/></svg><svg width="12" height="8"><use href="#ic-wifi"/></svg><svg width="16" height="8"><use href="#ic-battery"/></svg></span></div>
        <div class="topbar"><svg width="13" height="13"><use href="#ic-undo"/></svg><svg width="13" height="13"><use href="#ic-filter"/></svg></div>
        <article class="card">
          <div class="photo" style="height:296px" role="img" aria-label="Photo of a smiling caregiver with paint-covered hands in a colourful playroom">
            <div class="card-head"><div><div class="card-name">Marisol, $25/h <svg width="8" height="8"><use href="#ic-check"/></svg></div><div class="card-active"><span class="online"></span>Active today</div></div><span class="more">···</span></div>
            <div class="actions"><span class="act"><svg width="14" height="14"><use href="#ic-x"/></svg></span><span class="act"><svg width="16" height="16"><use href="#ic-star"/></svg></span><span class="act wave"><svg width="18" height="18"><use href="#ic-wave"/></svg></span></div>
          </div>
          <div class="prompt"><p class="prompt-q">One thing I prioritize in childcare is</p><p class="prompt-a">Creating a fun and engaging atmosphere where children can explore, play, and express themselves creatively</p></div>
        </article>
        <nav class="tabs"><span class="tab-brand"></span><svg width="12" height="12"><use href="#ic-trophy"/></svg><svg width="12" height="12"><use href="#ic-search"/></svg><svg width="12" height="12"><use href="#ic-chat"/></svg><span class="avatar"></span></nav>
        <div class="home-bar"></div>
      </div>
    </section>

    <!-- profile v2 -->
    <section class="slot">
      <h2 class="slot-label">Profile V2</h2>
      <div class="screen">
        <div class="status"><span>9:41</span><span class="status-icons"><svg width="12" height="8"><use href="#ic-signal"/></svg><svg width="12" height="8"><use href="#ic-wifi"/></svg><svg width="16" height="8"><use href="#ic-battery"/></svg></span></div>
        <header class="profile-head"><svg width="12" height="12"><use href="#ic-close"/></svg><div class="profile-title"><div class="profile-name">Marisol</div><div class="profile-active"><span class="online"></span>Active</div></div><span class="more" style="color:#9aa1ad">···</span></header>
        <ul class="facts" style="list-style:none">
          <li class="fact stats"><span class="stat"><svg width="10" height="10"><use href="#ic-bag"/></svg>10 yrs</span><span class="stat"><svg width="10" height="10"><use href="#ic-person"/></svg>Female</span><span class="stat"><svg width="10" height="10"><use href="#ic-coin"/></svg>25–35/h</span><span class="stat"><svg width="10" height="10"><use href="#ic-rate"/></svg>4.8</span></li>
          <li class="fact"><svg width="10" height="10"><use href="#ic-pin"/></svg>Cedar Vale, California</li>
          <li class="fact"><svg width="10" height="10"><use href="#ic-lang"/></svg>English, Spanish, Mandarin</li>
          <li class="fact"><svg width="10" height="10"><use href="#ic-degree"/></svg>Bachelor's Degree</li>
          <li class="fact"><svg width="10" height="10"><use href="#ic-child"/></svg>Age groups: <span class="chip">0–11 mo</span><span class="chip">1–3 yrs</span><span class="chip">4–5 yrs</span></li>
          <li class="fact"><svg width="10" height="10"><use href="#ic-kit"/></svg>CPR Trained, Special Needs Care</li>
          <li class="fact"><svg width="10" height="10"><use href="#ic-clock"/></svg>Full time, open to part time</li>
          <li class="fact"><svg width="10" height="10"><use href="#ic-warn"/></svg>Comfortable with pets, meal prep</li>
        </ul>
        <div class="profile-photo photo park" role="img" aria-label="Photo of the caregiver in a cap sitting in a sunny park">
          <div class="actions"><span class="act"><svg width="14" height="14"><use href="#ic-x"/></svg></span><span class="act"><svg width="16" height="16"><use href="#ic-star"/></svg></span><span class="act wave"><svg width="18" height="18"><use href="#ic-wave"/></svg></span></div>
        </div>
        <div class="home-bar" style="background:var(--white)"></div>
      </div>
    </section>
  </div>
</main>
</body>
</html>
```